Brochures for Sheds and Cabins

We require a brochure design for our cabin. We currently have an outdated brochure but this doesn't suit our website style. We want something more modern to match our website www.quillanbarns.co.nz. The specifications for this model is on our website link https://quillanbarns.co.nz/collections/lodge-range/products/harbour-room. The purpose of the brochure is to sell the cabin to the client making them desirable. We need the same contact information as the old brochure but we need it to be redesigned with a modern look. Ideal aspects we need it to feature is product prices, name, product info, images, and finance available, bespoke sheds and cabins, tailor made.

Target Market(s)

Home owners, Parents with Teenagers, Working from home people. Self Employed.

Colors

Designer to choose colors to be used in the design.

Requirements
Must have
• Must have modern look which matches website.
• Clear specifications on the product
• Creative Design

```html
<!DOCTYPE html>
<html lang="en">
<head>
<meta charset="utf-8">
<title>Quillan Barns – Cabins, Studios &amp; Sheds Brochures</title>
<link href="https://fonts.googleapis.com/css2?family=Oswald:wght@400;500;600;700&family=Open+Sans:wght@400;600&display=swap" rel="stylesheet">
<style>
:root{
  --ink:#151515;
  --paper:#f3f3f2;
  --panel:#fbfbfa;
  --brand:#2f78b7;
  --chip:#6d8aa4;
  --muted:#5a5a5a;
  --gap:#ffffff;
}
*{box-sizing:border-box;margin:0;padding:0}
html,body{width:1061px;height:1200px;overflow:hidden;background:var(--gap)}
.sheet{display:grid;grid-template-columns:repeat(5,1fr);grid-template-rows:repeat(4,1fr);gap:1px;width:1061px;height:1200px}
.brochure{position:relative;overflow:hidden;background:linear-gradient(160deg,var(--panel),var(--paper));font-family:"Open Sans",sans-serif;color:var(--ink)}
.photo{position:absolute;left:0;top:0;width:100%;height:130px}
.tone-dark{background:linear-gradient(135deg,#3b3a3c 0%,#6b6e70 45%,#a88a62 100%)}
.tone-grey{background:linear-gradient(135deg,#8c949b 0%,#c9cdd0 50%,#6f7a62 100%)}
.tone-light{background:linear-gradient(135deg,#c6c9cc 0%,#e4e4e2 55%,#7c6a55 100%)}
.tone-coast{background:linear-gradient(135deg,#5f7c4c 0%,#cfd6da 50%,#8fa6b6 100%)}
.tone-timber{background:linear-gradient(135deg,#49603a 0%,#a98e62 55%,#d2b887 100%)}
.tone-golden{background:linear-gradient(135deg,#6f7c88 0%,#c6a15a 50%,#e1c487 100%)}
.tone-garden{background:linear-gradient(135deg,#3e5a2c 0%,#9e8e6c 55%,#c8c2b2 100%)}
.title{position:absolute;left:9px;top:68px;width:84px;height:86px;padding:6px 6px;background:var(--ink);outline:1px solid #fff;outline-offset:-4px;display:flex;flex-direction:column;justify-content:center;align-items:center;text-align:center;color:#fff;font-family:"Oswald",sans-serif;font-weight:500;text-transform:uppercase;line-height:1.08;letter-spacing:-.2px;white-space:nowrap}
.title span{display:block}
.title .big{font-size:19px}
.title .long{font-size:16px}
.title .xlong{font-size:14.5px}
.title .mid{font-size:14px}
.title .sub{font-size:11px}
.title .small{font-size:9px}
.label{position:absolute;left:11px;font-family:"Oswald",sans-serif;font-weight:600;font-size:7px;color:var(--brand);text-transform:uppercase;letter-spacing:.1px}
.label.price-label{top:165px}
.label.size-label{top:203px}
.price{position:absolute;left:11px;top:175px;font-family:"Oswald",sans-serif;font-weight:600;font-size:14px}
.note{position:absolute;left:11px;top:214px;width:80px;font-size:3.4px;line-height:1.3;color:var(--muted)}
.sizes{position:absolute;left:11px;top:230px;display:flex;gap:2px}
.size{width:19px;height:22px;background:var(--chip);color:#fff;text-align:center;font-family:"Oswald",sans-serif;line-height:1;overflow:hidden}
.size b{display:block;font-size:3.2px;font-weight:500;padding-top:2px}
.size span{display:block;font-size:4.8px;font-weight:600;padding-top:2px}
.size i{display:block;font-size:2.8px;font-style:normal;padding-top:1px}
.info{position:absolute;left:100px;top:140px;width:106px}
.info h3{font-family:"Oswald",sans-serif;font-weight:600;font-size:7px;color:var(--brand);margin-bottom:4px}
.info p{font-size:3.6px;line-height:1.35;color:#333}
.footer{position:absolute;left:11px;right:8px;top:274px;display:flex;justify-content:space-between;align-items:center}
.brand{display:flex;align-items:center;gap:2px;font-family:"Oswald",sans-serif;font-weight:600;font-size:6.5px;color:var(--brand)}
.brand::before{content:"";width:5px;height:5px;background:var(--brand)}
.contact{font-size:3.3px;line-height:1.3;text-align:right;color:#333}
</style>
</head>
<body>
<main class="sheet">

<!-- Row 1 -->
<article class="brochure">
  <div class="photo tone-dark" role="img" aria-label="Dark clad studio with white bifold doors on a timber deck"></div>
  <h2 class="title"><span class="big">Classic</span><span class="big">Bifold</span><span class="big">Studio</span></h2>
  <p class="label price-label">Prices starting from</p><p class="price">$15,500</p>
  <p class="label size-label">We offer a range of sizes:</p>
  <p class="note">Sizes exclude additional deck and overhang length. Custom sizes – enquire within for pricing</p>
  <div class="sizes"><div class="size"><b>3.0M X 2.4M</b><span>$15,500</span><i>incl GST</i></div><div class="size"><b>4.0M X 2.4M</b><span>$15,700</span><i>incl GST</i></div><div class="size"><b>3.6M X 3.0M</b><span>$16,500</span><i>incl GST</i></div></div>
  <section class="info"><h3>PRODUCT INFO</h3><p>Monopitch Roof – 2.4m sloping back to 2.1m<br>NZ H3.2 Treated Pine Exterior Cladding<br>75 x 50 Dressed Pine Framing<br>1 x Aluminium 3-Fold Bifold Door<br>1 x Aluminium Awning Window<br>Corrugated Coloured Steel Roofing<br>Deck – 1000mm<br>Plywood Floor – 19mm<br>Lined with Building Paper<br>Interior Lined with V Groove Plywood</p></section>
  <footer class="footer"><span class="brand">QUILLAN BARNS LTD</span><span class="contact">48 TIDEWATER RD, MANUKAU | PH: 0800 555 019<br>SALES@QUILLANBARNS.CO.NZ | WWW.QUILLANBARNS.CO.NZ</span></footer>
</article>

<article class="brochure">
  <div class="photo tone-light" role="img" aria-label="Light weatherboard cabin with glass bifold doors"></div>
  <h2 class="title"><span class="long">Ultimate</span><span class="big">Bifold</span><span class="big">Cabin</span></h2>
  <p class="label price-label">Prices starting from</p><p class="price">$17,500</p>
  <p class="label size-label">We offer a range of sizes:</p>
  <p class="note">Sizes exclude additional deck and overhang length. Custom sizes – enquire within for pricing</p>
  <div class="sizes"><div class="size"><b>3.0M X 2.4M</b><span>$17,500</span><i>incl GST</i></div><div class="size"><b>4.0M X 2.4M</b><span>$17,700</span><i>incl GST</i></div></div>
  <section class="info"><h3>PRODUCT INFO</h3><p>Monopitch Roof – 2.4m sloping back to 2.1m<br>Prepainted Weatherboard Exterior Cladding<br>75 x 50 Dressed Pine Framing<br>1 x Aluminium 4-Fold Bifold Door<br>1 x Aluminium Awning Window<br>Corrugated Coloured Steel Roofing<br>Deck – 1000mm<br>Plywood Floor – 19mm<br>Lined with Building Paper<br>Interior Lined with V Groove Plywood</p></section>
  <footer class="footer"><span class="brand">QUILLAN BARNS LTD</span><span class="contact">48 TIDEWATER RD, MANUKAU | PH: 0800 555 019<br>SALES@QUILLANBARNS.CO.NZ | WWW.QUILLANBARNS.CO.NZ</span></footer>
</article>

<article class="brochure">
  <div class="photo tone-timber" role="img" aria-label="Natural timber cabin with sliding glass door and palm garden"></div>
  <h2 class="title"><span class="big">Fresh</span><span class="big">Space</span><span class="big">Cabin</span></h2>
  <p class="label price-label">Prices starting from</p><p class="price">$17,500</p>
  <p class="label size-label">We offer a range of sizes:</p>
  <p class="note">Sizes exclude additional deck and overhang length. Custom sizes – enquire within for pricing</p>
  <div class="sizes"><div class="size"><b>3.0M X 2.4M</b><span>$17,500</span><i>incl GST</i></div><div class="size"><b>4.0M X 2.4M</b><span>$17,700</span><i>incl GST</i></div></div>
  <section class="info"><h3>PRODUCT INFO</h3><p>Monopitch Roof – 2.4m sloping back to 2.1m<br>NZ H3.2 Treated Pine Exterior Cladding<br>75 x 50 Dressed Pine Framing<br>1 x Aluminium 3-Fold Bifold Door<br>1 x Aluminium Double Awning Window<br>Corrugated Coloured Steel Roofing<br>Deck – 1000mm<br>Plywood Floor – 19mm<br>Lined with Building Paper<br>Interior Lined with V Groove Plywood</p></section>
  <footer class="footer"><span class="brand">QUILLAN BARNS LTD</span><span class="contact">48 TIDEWATER RD, MANUKAU | PH: 0800 555 019<br>SALES@QUILLANBARNS.CO.NZ | WWW.QUILLANBARNS.CO.NZ</span></footer>
</article>

<article class="brochure">
  <div class="photo tone-grey" role="img" aria-label="Grey weatherboard cabin with double glazed windows"></div>
  <h2 class="title"><span class="long">Premium</span><span class="mid">Cabin W</span><span class="small">Double Glazing</span></h2>
  <p class="label price-label">Prices starting from</p><p class="price">$16,500</p>
  <p class="label size-label">We offer a range of sizes:</p>
  <p class="note">Sizes exclude additional deck and overhang length. Custom sizes – enquire within for pricing</p>
  <div class="sizes"><div class="size"><b>3.0M X 2.4M</b><span>$16,500</span><i>incl GST</i></div><div class="size"><b>4.0M X 2.4M</b><span>$16,700</span><i>incl GST</i></div><div class="size"><b>3.6M X 3.0M</b><span>$17,500</span><i>incl GST</i></div></div>
  <section class="info"><h3>PRODUCT INFO</h3><p>Monopitch Roof – 2.4m sloping back to 2.1m<br>Prepainted Weatherboard Exterior Cladding<br>75 x 50 Dressed Pine Framing<br>1 x Aluminium 3-Fold Bifold Door<br>Double Glazed Glass<br>Corrugated Coloured Steel Roofing<br>Deck – 1000mm<br>Plywood Floor – 19mm<br>Lined with Building Paper<br>Insulation in Walls and Roof</p></section>
  <footer class="footer"><span class="brand">QUILLAN BARNS LTD</span><span class="contact">48 TIDEWATER RD, MANUKAU | PH: 0800 555 019<br>SALES@QUILLANBARNS.CO.NZ | WWW.QUILLANBARNS.CO.NZ</span></footer>
</article>

<article class="brochure">
  <div class="photo tone-timber" role="img" aria-label="Board and batten timber cabin beside a grey fence"></div>
  <h2 class="title"><span class="xlong">Executive</span><span class="big">Cabin</span></h2>
  <p class="label price-label">Prices starting from</p><p class="price">$14,000</p>
  <p class="label size-label">We offer a range of sizes:</p>
  <p class="note">Sizes exclude additional deck and overhang length. Custom sizes – enquire within for pricing</p>
  <div class="sizes"><div class="size"><b>2.4M X 2.4M</b><span>$14,000</span><i>incl GST</i></div><div class="size"><b>3.0M X 2.4M</b><span>$14,400</span><i>incl GST</i></div><div class="size"><b>3.6M X 2.4M</b><span>$15,000</span><i>incl GST</i></div></div>
  <section class="info"><h3>PRODUCT INFO</h3><p>Monopitch Roof – 2.4m sloping back to 2.1m<br>Pine Board and Batten Exterior Cladding<br>75 x 50 Dressed Pine Framing<br>1 x Aluminium Sliding Door<br>1 x Aluminium Single Awning Window<br>Corrugated Coloured Steel Roofing<br>Deck/Step – 500mm<br>Plywood Floor – 19mm<br>Lined with Building Paper<br>Interior Lined with V Groove Plywood</p></section>
  <footer class="footer"><span class="brand">QUILLAN BARNS LTD</span><span class="contact">48 TIDEWATER RD, MANUKAU | PH: 0800 555 019<br>SALES@QUILLANBARNS.CO.NZ | WWW.QUILLANBARNS.CO.NZ</span></footer>
</article>

<!-- Row 2 -->
<article class="brochure">
  <div class="photo tone-coast" role="img" aria-label="White cottage cabin with veranda overlooking the sea"></div>
  <h2 class="title"><span class="big">Lined</span><span class="big">Cottage</span><span class="big">Cabin</span></h2>
  <p class="label price-label">Prices starting from</p><p class="price">$9,300</p>
  <p class="label size-label">We offer a range of sizes:</p>
  <p class="note">Sizes exclude additional deck and overhang length. Custom sizes – enquire within for pricing</p>
  <div class="sizes"><div class="size"><b>3.0M X 2.4M</b><span>$9,300</span><i>incl GST</i></div><div class="size"><b>3.6M X 2.4M</b><span>$9,800</span><i>incl GST</i></div><div class="size"><b>4.0M X 2.4M</b><span>$10,600</span><i>incl GST</i></div></div>
  <section class="info"><h3>PRODUCT INFO</h3><p>Gable Pitch Roof – 2.4m<br>NZ H3.2 Treated Pine Exterior Cladding<br>75 x 50 Dressed Pine Framing<br>1 x Full Cottage Double Door<br>2 x Wooden Single Fixed Windows<br>Corrugated Coloured Steel Roofing<br>Veranda – 1000mm<br>Plywood Floor – 19mm<br>Lined with Building Paper<br>Interior Lined with V Groove Plywood</p></section>
  <footer class="footer"><span class="brand">QUILLAN BARNS LTD</span><span class="contact">48 TIDEWATER RD, MANUKAU | PH: 0800 555 019<br>SALES@QUILLANBARNS.CO.NZ | WWW.QUILLANBARNS.CO.NZ</span></footer>
</article>

<article class="brochure">
  <div class="photo tone-grey" role="img" aria-label="Grey weatherboard cabin with French doors in a garden"></div>
  <h2 class="title"><span class="big">Kiwi</span><span class="big">Cabin</span></h2>
  <p class="label price-label">Prices starting from</p><p class="price">$13,500</p>
  <p class="label size-label">We offer a range of sizes:</p>
  <p class="note">Sizes exclude additional deck and overhang length. Custom sizes – enquire within for pricing</p>
  <div class="sizes"><div class="size"><b>3.0M X 2.4M</b><span>$13,500</span><i>incl GST</i></div><div class="size"><b>3.6M X 2.4M</b><span>$13,900</span><i>incl GST</i></div><div class="size"><b>3.6M X 3.0M</b><span>$15,000</span><i>incl GST</i></div></div>
  <section class="info"><h3>PRODUCT INFO</h3><p>Monopitch Roof – 2.4m sloping back to 2.1m<br>Weatherboard Exterior Cladding<br>75 x 50 Dressed Pine Framing<br>1 x Aluminium French Double Door<br>1 x Aluminium Double Awning Window<br>Corrugated Coloured Steel Roofing<br>Deck – 1000mm<br>Plywood Floor – 19mm<br>Lined with Building Paper<br>Interior Lined with V Groove Plywood</p></section>
  <footer class="footer"><span class="brand">QUILLAN BARNS LTD</span><span class="contact">48 TIDEWATER RD, MANUKAU | PH: 0800 555 019<br>SALES@QUILLANBARNS.CO.NZ | WWW.QUILLANBARNS.CO.NZ</span></footer>
</article>

<article class="brochure">
  <div class="photo tone-light" role="img" aria-label="White weatherboard studio with PVC joinery on a dark deck"></div>
  <h2 class="title"><span class="big">Crafted</span><span class="big">Studio</span><span class="small">With</span><span class="small">PVC Joinery</span></h2>
  <p class="label price-label">Prices starting from</p><p class="price">$13,500</p>
  <p class="label size-label">We offer a range of sizes:</p>
  <p class="note">Sizes exclude additional deck and overhang length. Custom sizes – enquire within for pricing</p>
  <div class="sizes"><div class="size"><b>3.0M X 2.4M</b><span>$13,500</span><i>incl GST</i></div><div class="size"><b>3.6M X 2.4M</b><span>$13,900</span><i>incl GST</i></div><div class="size"><b>3.6M X 3.0M</b><span>$14,600</span><i>incl GST</i></div></div>
  <section class="info"><h3>PRODUCT INFO</h3><p>Monopitch Roof – 2.4m sloping back to 2.1m<br>Prepainted Bevel Back Weatherboard<br>75 x 50 Dressed Pine Framing<br>1 x PVC French Double Door<br>1 x PVC Double Awning Window<br>PVC Joinery Colour – Arctic White<br>Deck – 1000mm<br>Plywood Floor – 19mm<br>Lined with Building Paper<br>Interior Lined with V Groove Plywood</p></section>
  <footer class="footer"><span class="brand">QUILLAN BARNS LTD</span><span class="contact">48 TIDEWATER RD, MANUKAU | PH: 0800 555 019<br>SALES@QUILLANBARNS.CO.NZ | WWW.QUILLANBARNS.CO.NZ</span></footer>
</article>

<article class="brochure">
  <div class="photo tone-golden" role="img" aria-label="Timber studio with a row of open awning windows"></div>
  <h2 class="title"><span class="big">Art</span><span class="big">Studio</span></h2>
  <p class="label price-label">Prices starting from</p><p class="price">$12,990</p>
  <p class="label size-label">We offer a range of sizes:</p>
  <p class="note">Sizes exclude additional deck and overhang length. Custom sizes – enquire within for pricing</p>
  <div class="sizes"><div class="size"><b>3.0M X 2.4M</b><span>$12,990</span><i>incl GST</i></div><div class="size"><b>3.6M X 2.4M</b><span>$13,390</span><i>incl GST</i></div><div class="size"><b>3.6M X 3.0M</b><span>$14,990</span><i>incl GST</i></div></div>
  <section class="info"><h3>PRODUCT INFO</h3><p>Monopitch Roof – 2.4m sloping back to 2.1m<br>NZ H3.2 Treated Pine Exterior Cladding<br>75 x 50 Dressed Pine Framing<br>1 x Aluminium French Double Door<br>4 x Aluminium Single Awning Windows<br>Corrugated Coloured Steel Roofing<br>Deck – 1000mm<br>Plywood Floor – 19mm<br>Lined with Building Paper<br>Interior Lined with V Groove Plywood</p></section>
  <footer class="footer"><span class="brand">QUILLAN BARNS LTD</span><span class="contact">48 TIDEWATER RD, MANUKAU | PH: 0800 555 019<br>SALES@QUILLANBARNS.CO.NZ | WWW.QUILLANBARNS.CO.NZ</span></footer>
</article>

<article class="brochure">
  <div class="photo tone-timber" role="img" aria-label="Timber studio with white joinery and outdoor chairs on a deck"></div>
  <h2 class="title"><span class="big">Modern</span><span class="long">Premium</span><span class="big">Studio</span></h2>
  <p class="label price-label">Prices starting from</p><p class="price">$12,500</p>
  <p class="label size-label">We offer a range of sizes:</p>
  <p class="note">Sizes exclude additional deck and overhang length. Custom sizes – enquire within for pricing</p>
  <div class="sizes"><div class="size"><b>3.0M X 2.4M</b><span>$12,500</span><i>incl GST</i></div><div class="size"><b>3.6M X 2.4M</b><span>$12,900</span><i>incl GST</i></div><div class="size"><b>3.6M X 3.0M</b><span>$13,600</span><i>incl GST</i></div></div>
  <section class="info"><h3>PRODUCT INFO</h3><p>Monopitch Roof – 2.4m sloping back to 2.1m<br>NZ H3.2 Treated Pine Exterior Cladding<br>75 x 50 Dressed Pine Framing<br>1 x Aluminium French Double Door<br>1 x Aluminium Double Awning Window<br>Corrugated Coloured Steel Roofing<br>Deck – 1000mm<br>Plywood Floor – 19mm<br>Lined with Building Paper<br>Interior Lined with V Groove Plywood</p></section>
  <footer class="footer"><span class="brand">QUILLAN BARNS LTD</span><span class="contact">48 TIDEWATER RD, MANUKAU | PH: 0800 555 019<br>SALES@QUILLANBARNS.CO.NZ | WWW.QUILLANBARNS.CO.NZ</span></footer>
</article>

<!-- Row 3 -->
<article class="brochure">
  <div class="photo tone-garden" role="img" aria-label="Timber combination shed with veranda in a green garden"></div>
  <h2 class="title"><span class="big">Classic</span><span class="sub">Combination</span><span class="big">Shed</span></h2>
  <p class="label price-label">Prices starting from</p><p class="price">$7,700</p>
  <p class="label size-label">We offer a range of sizes:</p>
  <p class="note">Sizes exclude additional deck and overhang length. Custom sizes – enquire within for pricing</p>
  <div class="sizes"><div class="size"><b>3.0M X 2.4M</b><span>$7,200</span><i>incl GST</i></div><div class="size"><b>3.6M X 2.4M</b><span>$8,100</span><i>incl GST</i></div><div class="size"><b>4.0M X 2.4M</b><span>$8,700</span><i>incl GST</i></div></div>
  <section class="info"><h3>PRODUCT INFO</h3><p>Gable Pitch Roof – 2.4m<br>NZ H3.2 Treated Pine Exterior Cladding<br>75 x 50 Dressed Pine Framing<br>1 x Full Cottage Double Door<br>1 x Aluminium Long Fixed Window<br>Corrugated Coloured Steel Roofing<br>Veranda – 1000mm<br>Plywood Floor – 19mm<br>Joists, Bearers</p></section>
  <footer class="footer"><span class="brand">QUILLAN BARNS LTD</span><span class="contact">48 TIDEWATER RD, MANUKAU | PH: 0800 555 019<br>SALES@QUILLANBARNS.CO.NZ | WWW.QUILLANBARNS.CO.NZ</span></footer>
</article>

<article class="brochure">
  <div class="photo tone-timber" role="img" aria-label="Timber villa cabin with paned windows among garden plants"></div>
  <h2 class="title"><span class="big">Lined</span><span class="big">Villa</span><span class="big">Cabin</span></h2>
  <p class="label price-label">Prices starting from</p><p class="price">$9,300</p>
  <p class="label size-label">We offer a range of sizes:</p>
  <p class="note">Sizes exclude additional deck and overhang length. Custom sizes – enquire within for pricing</p>
  <div class="sizes"><div class="size"><b>3.0M X 2.4M</b><span>$9,300</span><i>incl GST</i></div><div class="size"><b>3.6M X 2.4M</b><span>$9,800</span><i>incl GST</i></div><div class="size"><b>4.0M X 2.4M</b><span>$10,600</span><i>incl GST</i></div></div>
  <section class="info"><h3>PRODUCT INFO</h3><p>Gable Pitch Roof – 2.4m<br>NZ H3.2 Treated Pine Exterior Cladding<br>75 x 50 Dressed Pine Framing<br>1 x Half Timber Villa Double Door<br>3 x Wooden Single Fixed Windows<br>Corrugated Coloured Steel Roofing<br>Veranda – 1000mm<br>Plywood Floor – 19mm<br>Lined with Building Paper<br>Interior Lined with V Groove Plywood</p></section>
  <footer class="footer"><span class="brand">QUILLAN BARNS LTD</span><span class="contact">48 TIDEWATER RD, MANUKAU | PH: 0800 555 019<br>SALES@QUILLANBARNS.CO.NZ | WWW.QUILLANBARNS.CO.NZ</span></footer>
</article>

<article class="brochure">
  <div class="photo tone-golden" role="img" aria-label="Golden timber cabin with an extended veranda"></div>
  <h2 class="title"><span class="big">Large</span><span class="mid">Cabin W</span><span class="small">Extended Veranda</span></h2>
  <p class="label price-label">Prices starting from</p><p class="price">$8,200</p>
  <p class="label size-label">We offer a range of sizes:</p>
  <p class="note">Sizes exclude additional deck and overhang length. Custom sizes – enquire within for pricing</p>
  <div class="sizes"><div class="size"><b>3.0M X 2.4M</b><span>$8,200</span><i>incl GST</i></div><div class="size"><b>3.6M X 2.4M</b><span>$8,900</span><i>incl GST</i></div></div>
  <section class="info"><h3>PRODUCT INFO</h3><p>Gable Pitch Roof – 2.4m<br>NZ H3.2 Treated Pine Exterior Cladding<br>75 x 50 Dressed Pine Framing<br>1 x Half Timber Villa Double Door<br>2 x Wooden Double Opening Windows<br>Corrugated Coloured Steel Roofing<br>Overhang – 1000mm<br>Plywood Floor – 19mm<br>Joists, Bearers</p></section>
  <footer class="footer"><span class="brand">QUILLAN BARNS LTD</span><span class="contact">48 TIDEWATER RD, MANUKAU | PH: 0800 555 019<br>SALES@QUILLANBARNS.CO.NZ | WWW.QUILLANBARNS.CO.NZ</span></footer>
</article>

<article class="brochure">
  <div class="photo tone-dark" role="img" aria-label="Timber cottage shed with double doors on a deck"></div>
  <h2 class="title"><span class="big">Double</span><span class="mid">Door</span><span class="small">Cottage Shed</span></h2>
  <p class="label price-label">Prices starting from</p><p class="price">$7,900</p>
  <p class="label size-label">We offer a range of sizes:</p>
  <p class="note">Sizes exclude additional deck and overhang length. Custom sizes – enquire within for pricing</p>
  <div class="sizes"><div class="size"><b>3.0M X 2.4M</b><span>$7,900</span><i>incl GST</i></div><div class="size"><b>3.6M X 2.4M</b><span>$8,300</span><i>incl GST</i></div><div class="size"><b>4.0M X 2.4M</b><span>$8,900</span><i>incl GST</i></div></div>
  <section class="info"><h3>PRODUCT INFO</h3><p>Gable Pitch Roof – 2.4m<br>NZ H3.2 Treated Pine Exterior Cladding<br>75 x 50 Dressed Pine Framing<br>1 x Full Villa Double Door<br>2 x Wooden Single Fixed Windows<br>Corrugated Coloured Steel Roofing<br>Deck – 1000mm<br>Plywood Floor – 19mm<br>Joists, Bearers</p></section>
  <footer class="footer"><span class="brand">QUILLAN BARNS LTD</span><span class="contact">48 TIDEWATER RD, MANUKAU | PH: 0800 555 019<br>SALES@QUILLANBARNS.CO.NZ | WWW.QUILLANBARNS.CO.NZ</span></footer>
</article>

<article class="brochure">
  <div class="photo tone-garden" role="img" aria-label="Timber hobby shed with paned doors in a leafy garden"></div>
  <h2 class="title"><span class="big">Classic</span><span class="big">Hobby</span><span class="big">Shed</span></h2>
  <p class="label price-label">Prices starting from</p><p class="price">$7,700</p>
  <p class="label size-label">We offer a range of sizes:</p>
  <p class="note">Sizes exclude additional deck and overhang length. Custom sizes – enquire within for pricing</p>
  <div class="sizes"><div class="size"><b>3.0M X 2.4M</b><span>$7,200</span><i>incl GST</i></div><div class="size"><b>3.6M X 2.4M</b><span>$7,600</span><i>incl GST</i></div><div class="size"><b>4.0M X 2.4M</b><span>$8,200</span><i>incl GST</i></div></div>
  <section class="info"><h3>PRODUCT INFO</h3><p>Gable Pitch Roof – 2.4m<br>NZ H3.2 Treated Pine Exterior Cladding<br>75 x 50 Dressed Pine Framing<br>1 x Full Perspex Double Door<br>2 x Wooden Double Opening Windows<br>Corrugated Coloured Steel Roofing<br>Deck – 1000mm<br>Plywood Floor – 19mm<br>Joists, Bearers</p></section>
  <footer class="footer"><span class="brand">QUILLAN BARNS LTD</span><span class="contact">48 TIDEWATER RD, MANUKAU | PH: 0800 555 019<br>SALES@QUILLANBARNS.CO.NZ | WWW.QUILLANBARNS.CO.NZ</span></footer>
</article>

<!-- Row 4 -->
<article class="brochure">
  <div class="photo tone-garden" role="img" aria-label="Small timber garden shed with a door beside a fence"></div>
  <h2 class="title"><span class="big">Classic</span><span class="sub">Small Garden</span><span class="big">Shed</span></h2>
  <p class="label price-label">Prices starting from</p><p class="price">$3,200</p>
  <p class="label size-label">We offer a range of sizes:</p>
  <p class="note">Custom sizes – enquire within for pricing</p>
  <div class="sizes"><div class="size"><b>1.8M X 1.8M</b><span>$3,200</span><i>incl GST</i></div><div class="size"><b>2.4M X 1.8M</b><span>$3,400</span><i>incl GST</i></div><div class="size"><b>2.4M X 2.4M</b><span>$3,800</span><i>incl GST</i></div></div>
  <section class="info"><h3>PRODUCT INFO</h3><p>Gable Pitch Roof – 2.4m<br>NZ H3.2 Treated Pine Exterior Cladding<br>75 x 50 Dressed Pine Framing<br>1 x Full Cottage Double Door<br>Corrugated Coloured Steel Roofing<br>Lined with Building Paper<br>Plywood Floor – 19mm<br>Joists, Bearers</p></section>
  <footer class="footer"><span class="brand">QUILLAN BARNS LTD</span><span class="contact">48 TIDEWATER RD, MANUKAU | PH: 0800 555 019<br>SALES@QUILLANBARNS.CO.NZ | WWW.QUILLANBARNS.CO.NZ</span></footer>
</article>

<article class="brochure">
  <div class="photo tone-garden" role="img" aria-label="Timber cottage garden shed beside a hedge and lawn"></div>
  <h2 class="title"><span class="big">Large</span><span class="big">Cottage</span><span class="sub">Garden Shed</span></h2>
  <p class="label price-label">Prices starting from</p><p class="price">$7,200</p>
  <p class="label size-label">We offer a range of sizes:</p>
  <p class="note">Sizes exclude additional deck and overhang length. Custom sizes – enquire within for pricing</p>
  <div class="sizes"><div class="size"><b>3.0M X 2.4M</b><span>$7,200</span><i>incl GST</i></div><div class="size"><b>3.6M X 2.4M</b><span>$7,600</span><i>incl GST</i></div><div class="size"><b>4.0M X 2.4M</b><span>$8,200</span><i>incl GST</i></div></div>
  <section class="info"><h3>PRODUCT INFO</h3><p>Gable Pitch Roof – 2.4m<br>NZ H3.2 Treated Pine Exterior Cladding<br>75 x 50 Dressed Pine Framing<br>1 x Full Cottage Double Door<br>2 x Wooden Double Fixed Windows<br>Corrugated Coloured Steel Roofing<br>Veranda – 1000mm<br>Plywood Floor – 19mm<br>Joists, Bearers</p></section>
  <footer class="footer"><span class="brand">QUILLAN BARNS LTD</span><span class="contact">48 TIDEWATER RD, MANUKAU | PH: 0800 555 019<br>SALES@QUILLANBARNS.CO.NZ | WWW.QUILLANBARNS.CO.NZ</span></footer>
</article>

<article class="brochure">
  <div class="photo tone-timber" role="img" aria-label="Timber villa garden shed with veranda and paned doors"></div>
  <h2 class="title"><span class="big">Villa</span><span class="big">Garden</span><span class="big">Shed</span></h2>
  <p class="label price-label">Prices starting from</p><p class="price">$7,200</p>
  <p class="label size-label">We offer a range of sizes:</p>
  <p class="note">Sizes exclude additional deck and overhang length. Custom sizes – enquire within for pricing</p>
  <div class="sizes"><div class="size"><b>3.0M X 2.4M</b><span>$7,200</span><i>incl GST</i></div><div class="size"><b>3.6M X 2.4M</b><span>$7,600</span><i>incl GST</i></div><div class="size"><b>4.0M X 2.4M</b><span>$8,200</span><i>incl GST</i></div><div class="size"><b>3.6M X 3.0M</b><span>$8,200</span><i>incl GST</i></div></div>
  <section class="info"><h3>PRODUCT INFO</h3><p>Gable Pitch Roof – 2.4m<br>NZ H3.2 Treated Pine Exterior Cladding<br>75 x 50 Dressed Pine Framing<br>1 x Half Timber Villa Double Door<br>3 x Wooden Single Fixed Windows<br>Corrugated Coloured Steel Roofing<br>Veranda – 1000mm<br>Plywood Floor – 19mm<br>Joists, Bearers</p></section>
  <footer class="footer"><span class="brand">QUILLAN BARNS LTD</span><span class="contact">48 TIDEWATER RD, MANUKAU | PH: 0800 555 019<br>SALES@QUILLANBARNS.CO.NZ | WWW.QUILLANBARNS.CO.NZ</span></footer>
</article>

<article class="brochure">
  <div class="photo tone-garden" role="img" aria-label="Standard timber garden shed in a backyard"></div>
  <h2 class="title"><span class="long">Standard</span><span class="big">Garden</span><span class="big">Shed</span></h2>
  <p class="label price-label">Prices starting from</p><p class="price">$4,290</p>
  <p class="label size-label">We offer a range of sizes:</p>
  <p class="note">Custom sizes – enquire within for pricing</p>
  <div class="sizes"><div class="size"><b>2.4M X 1.8M</b><span>$4,290</span><i>incl GST</i></div><div class="size"><b>2.4M X 2.4M</b><span>$4,870</span><i>incl GST</i></div><div class="size"><b>3.0M X 2.4M</b><span>$5,400</span><i>incl GST</i></div></div>
  <section class="info"><h3>PRODUCT INFO</h3><p>Gable Pitch Roof – 2.4m<br>NZ H3.2 Treated Pine Exterior Cladding<br>75 x 50 Dressed Pine Framing<br>1 x Full Timber Double Door<br>1 x Wooden Single Fixed Window<br>Corrugated Coloured Steel Roofing<br>Lined with Building Paper<br>Plywood Floor – 19mm<br>Joists, Bearers</p></section>
  <footer class="footer"><span class="brand">QUILLAN BARNS LTD</span><span class="contact">48 TIDEWATER RD, MANUKAU | PH: 0800 555 019<br>SALES@QUILLANBARNS.CO.NZ | WWW.QUILLANBARNS.CO.NZ</span></footer>
</article>

<article class="brochure">
  <div class="photo tone-light" role="img" aria-label="Small timber villa garden shed beside a white wall"></div>
  <h2 class="title"><span class="big">Small</span><span class="sub">Villa Garden</span><span class="big">Shed</span></h2>
  <p class="label price-label">Prices starting from</p><p class="price">$3,800</p>
  <p class="label size-label">We offer a range of sizes:</p>
  <p class="note">Custom sizes – enquire within for pricing</p>
  <div class="sizes"><div class="size"><b>1.8M X 1.8M</b><span>$3,800</span><i>incl GST</i></div><div class="size"><b>2.4M X 1.8M</b><span>$4,000</span><i>incl GST</i></div><div class="size"><b>2.4M X 2.4M</b><span>$4,200</span><i>incl GST</i></div></div>
  <section class="info"><h3>PRODUCT INFO</h3><p>Gable Pitch Roof – 2.4m<br>NZ H3.2 Treated Pine Exterior Cladding<br>75 x 50 Dressed Pine Framing<br>1 x Half Villa Double Door<br>2 x Wooden Single Fixed Windows<br>Corrugated Coloured Steel Roofing<br>Veranda – 750mm<br>Plywood Floor – 19mm<br>Joists, Bearers</p></section>
  <footer class="footer"><span class="brand">QUILLAN BARNS LTD</span><span class="contact">48 TIDEWATER RD, MANUKAU | PH: 0800 555 019<br>SALES@QUILLANBARNS.CO.NZ | WWW.QUILLANBARNS.CO.NZ</span></footer>
</article>

</main>
</body>
</html>
```